Vexo App

We want to have a web banner (4-5 slides) flash or whatever.
We are innovative next generation messenger with a good design, themes, snap mode, pinging and other features.
Inspired by night, by techno music, by energy, by innovations and next generation.
High tech.

The name of the app : Vexo
vexoapp.example

The banner will be used for nightlisting.example

We want the banner to be creative, and deliver the inspiration of the app.

All the assets, logos and so on can me delivered to you via email by request.

```html
<!DOCTYPE html>
<html lang="en">
<head>
<meta charset="utf-8">
<title>Vexo – Go Deep banner</title>
<link rel="stylesheet" href="https://fonts.googleapis.com/css2?family=Open+Sans:wght@400;600;700&display=swap">
<style>
  :root {
    --night: #07080c;
    --night-2: #12141b;
    --lime: #9fcf2a;
    --white: #f4f6f2;
    --glitch-green: #3fa83a;
    --glitch-blue: #2b3f8f;
  }
  html, body {
    margin: 0;
    padding: 0;
    width: 1200px;
    height: 148px;
    overflow: hidden;
    background: var(--night);
  }
  .banner {
    position: relative;
    width: 1200px;
    height: 148px;
    overflow: hidden;
    background: linear-gradient(180deg, var(--night-2) 0%, var(--night) 50%, var(--night-2) 100%);
    font-family: "Open Sans", Arial, sans-serif;
  }
  .glitch-field {
    position: absolute;
    inset: 0;
    background:
      radial-gradient(ellipse 120px 60px at 370px 55px, rgba(63,168,58,0.45), transparent 70%),
      radial-gradient(ellipse 90px 50px at 470px 30px, rgba(43,63,143,0.4), transparent 70%),
      radial-gradient(ellipse 160px 70px at 1080px 70px, rgba(63,168,58,0.5), transparent 70%),
      radial-gradient(ellipse 120px 50px at 960px 25px, rgba(43,63,143,0.45), transparent 70%),
      repeating-linear-gradient(180deg, rgba(255,255,255,0.03) 0 3px, transparent 3px 9px);
  }
  .brand {
    position: absolute;
    left: 58px;
    top: 50%;
    transform: translateY(-50%);
    display: flex;
    align-items: center;
    gap: 18px;
  }
  .brand-square {
    width: 56px;
    height: 56px;
    background: var(--lime);
  }
  .brand-name {
    color: var(--white);
    font-weight: 700;
    font-size: 34px;
    letter-spacing: 0.5px;
  }
  .tagline {
    position: absolute;
    left: 574px;
    top: 50%;
    transform: translateY(-52%);
    margin: 0;
    font-weight: 400;
    font-size: 40px;
    letter-spacing: 0.5px;
    color: var(--white);
    white-space: nowrap;
  }
  .tagline .accent { color: var(--lime); }
</style>
</head>
<body>
  <div class="banner">
    <div class="glitch-field" role="img" aria-label="Dark glitch texture of horizontal green and blue digital streaks"></div>
    <div class="brand">
      <div class="brand-square"></div>
      <span class="brand-name">Vexo</span>
    </div>
    <h1 class="tagline"><span class="accent">GO</span> DEEP</h1>
  </div>
</body>
</html>
```